Business Card Design

New business card design

Target Market(s)

Residential & Commercial Property Managers

Industry/Entity Type

Plumbing Services

Contact Information for Business Card

Name - Owen Tredgold, title - Director, Phone Number - 0431 862 507, email - owen@rvb-plumbing.com.au, Company ABN - 73 215 904 386,

Font styles to use
Sans Serif

Colors
0054AA
0677BA
7BADD7
CADEEF
E8F1F8

```html
<!DOCTYPE html>
<html lang="en">
<head>
<meta charset="utf-8">
<title>RVB Plumbing Services — Business Card</title>
<link rel="stylesheet" href="https://fonts.googleapis.com/css2?family=Roboto:wght@300;400;700&display=swap">
<style>
  :root {
    --bg: #1b1b1b;
    --blue-deep: #0a3f8a;
    --blue-brand: #0054aa;
    --blue-mid: #0677ba;
    --blue-sky: #3fa6d6;
    --blue-soft: #7badd7;
    --blue-pale: #cadeef;
    --blue-mist: #e8f1f8;
    --ink-dark: #1e1e1e;
    --white: #ffffff;
  }
  * { box-sizing: border-box; margin: 0; padding: 0; }
  html, body { width: 1200px; height: 852px; overflow: hidden; }
  body {
    background: var(--bg);
    font-family: "Roboto", Arial, sans-serif;
    position: relative;
  }
  .card {
    position: absolute;
    width: 520px;
    height: 300px;
    border-radius: 24px;
    overflow: hidden;
    background: var(--blue-brand);
    box-shadow: 0 10px 30px rgba(0,0,0,.5);
  }
  .card-front { left: 60px; top: 150px; }
  .card-back { left: 620px; top: 400px; }

  .card-backdrop { position: absolute; inset: 0; }
  .card-front .card-backdrop {
    background: linear-gradient(170deg, var(--blue-sky) 0%, var(--blue-mid) 35%, var(--blue-brand) 65%, var(--blue-deep) 100%);
  }
  .card-back .card-backdrop {
    background: linear-gradient(110deg, var(--blue-deep) 0%, var(--blue-deep) 40%, var(--blue-brand) 58%, var(--blue-mid) 78%, var(--blue-sky) 100%);
  }

  .brand { position: absolute; color: var(--white); font-weight: 300; display: flex; align-items: center; gap: 12px; }
  .brand-dot { width: 16px; height: 16px; border-radius: 50%; background: var(--white); flex: none; }
  .brand-name { font-size: 34px; letter-spacing: 1px; line-height: 1; white-space: nowrap; }
  .card-front .brand { left: 70px; top: 126px; }
  .card-back .brand { left: 36px; top: 52px; gap: 10px; }
  .card-back .brand-dot { width: 13px; height: 13px; }
  .card-back .brand-name { font-size: 24px; }

  .holder { position: absolute; left: 40px; top: 150px; color: var(--white); }
  .holder-name { font-size: 22px; font-weight: 700; line-height: 1.1; }
  .holder-title { font-size: 13px; font-weight: 300; color: var(--blue-mist); }
  .location { position: absolute; left: 40px; top: 248px; font-size: 12px; font-weight: 300; color: var(--blue-mist); letter-spacing: .5px; }

  .contacts { position: absolute; left: 300px; top: 100px; list-style: none; color: var(--white); font-size: 12px; font-weight: 300; }
  .contacts li { display: flex; align-items: center; gap: 8px; height: 17px; white-space: nowrap; }
  .contacts svg { width: 11px; height: 11px; fill: var(--blue-pale); flex: none; }

  .legal-band {
    position: absolute; right: 0; bottom: 0; width: 250px; height: 76px;
    background: var(--ink-dark);
    border-top-left-radius: 22px;
    display: flex; align-items: center; justify-content: center;
    color: var(--blue-mist); font-size: 12px; font-weight: 300;
  }
  .legal-accent { position: absolute; left: 0; top: 0; bottom: 0; width: 10px; background: var(--blue-sky); border-top-left-radius: 22px; }
</style>
</head>
<body>

  <section class="card card-front" aria-label="Card front">
    <div class="card-backdrop" role="img" aria-label="Layered blue water wave background"></div>
    <div class="brand">
      <span class="brand-dot"></span>
      <span class="brand-name">RVB Plumbing Services</span>
    </div>
  </section>

  <section class="card card-back" aria-label="Card back">
    <div class="card-backdrop" role="img" aria-label="Layered blue water wave background"></div>

    <div class="brand">
      <span class="brand-dot"></span>
      <span class="brand-name">RVB Plumbing Services</span>
    </div>

    <div class="holder">
      <p class="holder-name">Owen Tredgold</p>
      <p class="holder-title">Director</p>
    </div>

    <p class="location">Sydney &nbsp;|&nbsp; NSW &nbsp;|&nbsp; Australia</p>

    <ul class="contacts">
      <li><svg viewBox="0 0 24 24"><path d="M6.6 10.8a15 15 0 0 0 6.6 6.6l2.2-2.2a1 1 0 0 1 1-.25 11.4 11.4 0 0 0 3.6.57 1 1 0 0 1 1 1V20a1 1 0 0 1-1 1A17 17 0 0 1 3 4a1 1 0 0 1 1-1h3.5a1 1 0 0 1 1 1c0 1.25.2 2.45.57 3.57a1 1 0 0 1-.25 1z"/></svg>0431 862 507</li>
      <li><svg viewBox="0 0 24 24"><path d="M2 5h20v14H2z M2 5l10 8 10-8"/></svg>owen@rvb-plumbing.com.au</li>
      <li><svg viewBox="0 0 24 24"><circle cx="12" cy="12" r="10"/></svg>www.rvb-plumbing.com.au</li>
      <li><svg viewBox="0 0 24 24"><circle cx="12" cy="12" r="8"/></svg>ABN - 73 215 904 386</li>
    </ul>

    <div class="legal-band">
      <span class="legal-accent"></span>
      RVB Plumbing Services Pvt Ltd.
    </div>
  </section>

</body>
</html>
```